Company brochure for our unique consulting business

We are a small consulting business offering a unique set of services to our clients.. In simple terms we are a business improvement consultancy helping our clients get the best out of their businesses. We work with clients across multiple sectors and deliver a variety of services. We want to put together a brochure to cover these main themes:1. Who we are2. What we do3. The type of people we employ4. The sectors we work inWhile the brochure needs to have a certain corporate feel to it, we don't want it to be "boring" or "stiff". We would like it to have a slightly "friendly" or "informal" feel to it, to reflect the type of organisation we are.We have a company website http://tollandvergeadvisory.com , however we do not want to directly replicate the content or feel as we recognise it needs updating.We would like the brochure to be A4 portrait format. We anticipate requiring 12 sides (including covers) but we are happy to be guided on this based on the content we have provided.The attached ppt file gives the detail of the content to be included and also shows the proposed pagination. For the front cover we would like to try 2 versions, one with the TVA logo and one with the Tolland Verge Advisory logo (a file of both is attached)One of the most important pages will be the "Our Services" page. We would like this to cover the centre fold. In the ppt file we have shown an example layout, but this is where we need most help - we are clearly not graphic designers! This page will be the most used page in sales meetings etc.Also attached is the following:1. file for our TollandVerge Advisory company logo.2. File for our TVA company logo3. Files for Derek's signatures (for under photos) - Owen's to follow4. Photo of Derek & Owen (person in purple shirt to be cropped out)Thank you and really excited to see what everyone comes back with.Derek & Owen

Target Market(s)

Very broad - Manufacturing, Healthcare, Hospitality

Industry/Entity Type

Management Consulting

Font styles to use
Other font styles liked:
• We use Swiss721, but happy to be guided by designer

Colors
3276b5
85abd2
0355a3
333333
5c5c5c
9d9d9d
d9d9d9

Requirements
Must have
• Corporate feel
Nice to have
• Slightly friendly feel
• Our standard "blue" is (CORRECTION) - R55 G96 B146 #376092 and our standard grey is R197 G178, B179 - #B3B2B2, which we would like to keep, but other colours we are happy to be guided on. Brand guidelines attached.

```html
<!DOCTYPE html>
<html lang="en">
<head>
<meta charset="utf-8">
<title>Tolland Verge Advisory – Brochure Covers</title>
<link rel="stylesheet" href="https://fonts.googleapis.com/css2?family=Open+Sans:wght@700&family=Roboto+Condensed:wght@300;700&display=swap">
<style>
  :root {
    --brand-blue: #376092;
    --brand-blue-mid: #3276b5;
    --brand-blue-light: #85abd2;
    --ink: #111111;
    --charcoal: #333333;
    --paper: #ffffff;
    --stage: #dcdcdc;
  }
  * { margin: 0; padding: 0; box-sizing: border-box; }
  html, body {
    width: 1200px;
    height: 700px;
    overflow: hidden;
    background: var(--stage);
  }
  .spread {
    position: absolute;
    left: 176px;
    top: 50px;
    width: 848px;
    height: 600px;
    display: flex;
    box-shadow: 0 12px 34px rgba(0,0,0,0.2);
  }
  .cover {
    width: 424px;
    height: 600px;
    display: block;
  }
  .back-cover { border-right: 1px solid rgba(0,0,0,0.25); }
  .url {
    font-family: "Open Sans", sans-serif;
    font-weight: 700;
    font-size: 12px;
    letter-spacing: 0.5px;
    fill: var(--paper);
  }
  .wordmark {
    font-family: "Roboto Condensed", sans-serif;
    font-weight: 700;
    font-size: 52px;
    letter-spacing: 2px;
    fill: var(--charcoal);
  }
  .slogan-light {
    font-family: "Roboto Condensed", sans-serif;
    font-weight: 300;
    font-size: 32px;
    fill: var(--paper);
  }
  .slogan-bold {
    font-family: "Roboto Condensed", sans-serif;
    font-weight: 700;
    font-size: 40px;
    fill: var(--paper);
  }
</style>
</head>
<body>
<main class="spread">

  <!-- Back cover -->
  <svg class="cover back-cover" viewBox="0 0 424 600" xmlns="http://www.w3.org/2000/svg">
    <defs>
      <linearGradient id="railway-sky" x1="0" y1="0" x2="0" y2="1">
        <stop offset="0" stop-color="#b9607f"/>
        <stop offset="0.22" stop-color="#e0867a"/>
        <stop offset="0.34" stop-color="#f0a664"/>
        <stop offset="0.42" stop-color="#7a5d78"/>
        <stop offset="0.6" stop-color="#4a4a5c"/>
        <stop offset="1" stop-color="#262a33"/>
      </linearGradient>
      <radialGradient id="railway-glow" cx="0.55" cy="0.38" r="0.45">
        <stop offset="0" stop-color="#ffc36b" stop-opacity="0.75"/>
        <stop offset="1" stop-color="#ffc36b" stop-opacity="0"/>
      </radialGradient>
    </defs>
    <g class="photo railway" role="img" aria-label="Photo of a freight rail yard with tanker wagons at sunset">
      <rect x="0" y="0" width="424" height="490" fill="url(#railway-sky)"/>
      <rect x="0" y="0" width="424" height="490" fill="url(#railway-glow)"/>
    </g>
    <polygon class="photo-tint" points="300,0 424,0 424,490 200,490" fill="var(--brand-blue)" opacity="0.35"/>
    <polygon class="accent-strip" points="0,478 130,478 142,466 424,466 424,500 0,500" fill="var(--brand-blue)"/>
    <rect class="footer-band" x="0" y="500" width="424" height="100" fill="var(--ink)"/>
    <text class="url" x="212" y="555" text-anchor="middle">www.tollandvergeadvisory.com</text>
  </svg>

  <!-- Front cover -->
  <svg class="cover front-cover" viewBox="0 0 424 600" xmlns="http://www.w3.org/2000/svg">
    <defs>
      <linearGradient id="meeting-tones" x1="0" y1="0" x2="1" y2="1">
        <stop offset="0" stop-color="#eeebe6"/>
        <stop offset="0.45" stop-color="#dfe3ea"/>
        <stop offset="0.7" stop-color="#b9cde3"/>
        <stop offset="1" stop-color="#d9cfe3"/>
      </linearGradient>
      <radialGradient id="meeting-light" cx="0.6" cy="0.3" r="0.5">
        <stop offset="0" stop-color="#ffffff" stop-opacity="0.7"/>
        <stop offset="1" stop-color="#ffffff" stop-opacity="0"/>
      </radialGradient>
    </defs>
    <rect x="0" y="0" width="424" height="600" fill="var(--paper)"/>
    <rect class="logo-mark" x="120" y="52" width="40" height="40" fill="var(--brand-blue)"/>
    <text class="wordmark" x="172" y="92">TVA</text>
    <polygon class="header-rule" points="90,116 424,104 424,110 90,122" fill="var(--ink)"/>
    <g class="photo meeting" role="img" aria-label="Photo of the two founders smiling in a bright office meeting">
      <rect x="0" y="130" width="424" height="340" fill="url(#meeting-tones)"/>
      <rect x="0" y="130" width="424" height="340" fill="url(#meeting-light)"/>
    </g>
    <polygon class="slogan-panel" points="0,150 240,150 240,330 300,470 0,470" fill="var(--brand-blue)" opacity="0.92"/>
    <text class="slogan-light" x="22" y="210">BETTER</text>
    <text class="slogan-bold" x="22" y="252">PEOPLE</text>
    <text class="slogan-light" x="22" y="294">BETTER</text>
    <text class="slogan-bold" x="22" y="338">BUSINESS</text>
    <polygon class="accent-strip" points="0,470 330,470 342,458 424,458 424,484 0,484" fill="var(--brand-blue)"/>
    <rect class="footer-band" x="150" y="484" width="274" height="116" fill="var(--ink)"/>
    <text class="url" x="404" y="548" text-anchor="end">www.tollandvergeadvisory.com</text>
  </svg>

</main>
</body>
</html>
```